Car dent,ding,crease removal. This will be for the Automotive industry, bodywork repair.

I need a double sided business card designing.

Company name is Ding Mender and we remove small car park dents creases and dings.

The card should have sleek car design/outline on it.

The wording Paintless Dent Removal to be on the card.

The background colours used should include Royal blue, black, and a hint of red.

Need a sleek modern look, clean lines.

I really don't want designers going to my website and just copying the car design, I want something new!

Reason: I've put a guaranteed payment on the design now.

Automotive

Must have
• Paintless Dent Removal
Ding Mender
Gareth Holloway
enquiries@dingmender.co.uk
07912364580
Covering, Chester, North Wales and the Wirral
Free quotes available
www.dingmender.co.uk

```html
<!DOCTYPE html>
<html lang="en">
<head>
<meta charset="utf-8">
<title>Ding Mender – Business Card</title>
<link href="https://fonts.googleapis.com/css2?family=Roboto+Slab:wght@700&family=Open+Sans:wght@400;600&display=swap" rel="stylesheet">
<style>
  :root {
    --backdrop: #dcdcdc;
    --royal-blue: #1a4fd8;
    --royal-blue-light: #2763e6;
    --car-area-top: rgba(255,255,255,.16);
    --car-area-bottom: rgba(255,255,255,.05);
    --white: #ffffff;
    --soft-white: #e8eeff;
    --accent-red: #e3102a;
    --slab: "Roboto Slab", "Rockwell", serif;
    --sans: "Open Sans", Arial, sans-serif;
  }
  * { box-sizing: border-box; margin: 0; padding: 0; }
  html, body {
    width: 1200px; height: 800px; overflow: hidden;
    background: var(--backdrop);
  }
  .sheet {
    position: relative; width: 1200px; height: 800px;
    display: flex; align-items: center; justify-content: center; gap: 60px;
  }
  .card {
    position: relative; width: 520px; height: 297px;
    background: linear-gradient(135deg, var(--royal-blue-light), var(--royal-blue) 60%);
    color: var(--white);
    box-shadow: 0 2px 6px rgba(0,0,0,.18);
    font-family: var(--sans);
    overflow: hidden;
  }
  .icon { width: 14px; height: 14px; flex: none; }
  .icon path, .icon circle { fill: var(--accent-red); }
  .contact-line { display: flex; align-items: center; gap: 8px; white-space: nowrap; }

  /* Back: personal details */
  .card-back { padding-top: 50px; }
  .card-back .holder {
    text-align: center;
    font-family: var(--slab); font-weight: 700; font-size: 24px; letter-spacing: 1px;
  }
  .card-back .role {
    text-align: center; font-size: 9px; letter-spacing: 1.5px;
    text-transform: uppercase; color: var(--soft-white); margin-top: 2px;
  }
  .card-back .details { margin: 34px 0 0 150px; font-size: 12.5px; line-height: 1.5; }
  .card-back .coverage { margin-top: 12px; }

  /* Front: brand */
  .car-outline {
    position: absolute; left: 70px; right: 70px; top: 30px; height: 108px;
    background: linear-gradient(180deg, var(--car-area-top), var(--car-area-bottom));
    border-radius: 60px 80px 6px 6px;
  }
  .red-rule {
    position: absolute; left: 50px; right: 50px; top: 142px; height: 3px;
    background: var(--accent-red);
  }
  .brand-name {
    position: absolute; left: 0; right: 0; top: 152px; text-align: center;
    font-family: var(--slab); font-weight: 700; font-size: 26px; letter-spacing: 3px;
    text-transform: uppercase; color: var(--white);
  }
  .front-contacts {
    position: absolute; left: 40px; right: 40px; bottom: 26px;
    display: flex; justify-content: space-between; align-items: flex-end;
    font-size: 12px; line-height: 1.6;
  }
</style>
</head>
<body>
<main class="sheet">
  <section class="card card-back" aria-label="Card back">
    <h1 class="holder">GARETH HOLLOWAY</h1>
    <p class="role">Paintless Dent Removal Technician</p>
    <div class="details">
      <p class="contact-line">
        <svg class="icon" viewBox="0 0 16 16"><path d="M3 1h3l1.5 4-2 1.3a8 8 0 0 0 4.2 4.2L11 8.5l4 1.5v3a2 2 0 0 1-2 2A12 12 0 0 1 1 3a2 2 0 0 1 2-2z"/></svg>
        079 123 645 80
      </p>
      <p class="contact-line">
        <svg class="icon" viewBox="0 0 16 16"><path d="M1 3h14v10H1zM2.5 4.5v.4L8 9l5.5-4.1v-.4z"/></svg>
        enquiries@dingmender.co.uk
      </p>
      <p class="coverage">Covering, Chester, North Wales<br>and the Wirral.<br>Free quotes available.</p>
      <p>www.dingmender.co.uk</p>
    </div>
  </section>

  <section class="card card-front" aria-label="Card front">
    <div class="car-outline" role="img" aria-label="Sleek white line drawing of a sports car in side profile"></div>
    <div class="red-rule"></div>
    <p class="brand-name">Ding Mender</p>
    <div class="front-contacts">
      <div>
        <p class="contact-line">
          <svg class="icon" viewBox="0 0 16 16"><circle cx="8" cy="4.5" r="3.5"/><path d="M1.5 15a6.5 6 0 0 1 13 0z"/></svg>
          Gareth Holloway
        </p>
        <p class="contact-line">
          <svg class="icon" viewBox="0 0 16 16"><path d="M3 1h3l1.5 4-2 1.3a8 8 0 0 0 4.2 4.2L11 8.5l4 1.5v3a2 2 0 0 1-2 2A12 12 0 0 1 1 3a2 2 0 0 1 2-2z"/></svg>
          079-123-645-80
        </p>
      </div>
      <div>
        <p class="contact-line">
          <svg class="icon" viewBox="0 0 16 16"><path d="M1 3h14v10H1zM2.5 4.5v.4L8 9l5.5-4.1v-.4z"/></svg>
          enquiries@dingmender.co.uk
        </p>
        <p class="contact-line">
          <svg class="icon" viewBox="0 0 16 16"><path d="M8 1a7 7 0 1 0 0 14A7 7 0 0 0 8 1zm0 1.6c.8.9 1.4 2.2 1.6 3.7H6.4C6.6 4.8 7.2 3.5 8 2.6zM2.7 7.7h2.3a12 12 0 0 0 .5 3.6H3.8a5.4 5.4 0 0 1-1.1-3.6zm8.3 0h2.3a5.4 5.4 0 0 1-1.1 3.6h-1.7a12 12 0 0 0 .5-3.6zM6.4 7.7h3.2a10 10 0 0 1-.5 3.6H6.9a10 10 0 0 1-.5-3.6z"/></svg>
          www.dingmender.co.uk
        </p>
      </div>
    </div>
  </section>
</main>
</body>
</html>
```